Window Treatment business needs website redesigned.

We need a revamp and refresh of our current site www.velmarblinds.ca
Looking to attract very high end customer. It should be a very simple design with very little text. This site will be visited by prospective homeowners, designers, builders and architects. They should feel that they are dealing with a high-end product selection, where experience, customer service and unique product offering is the focus. The content will be to highlight our services and highlight the manufacturers we sell, using a few rich photos to highlight the products. We should NOT look like we are a very large company. It should NOT have discounts/savings buttons and many menus to choose from. We offer over 15 years experience to narrow the many market options, to provide the right technical solution.
We specialize in products that are not readily available on the market and specifically motorized systems for indoors and outdoors.
Our main suppliers are Kervanto.com, Brindex.com
We carry our own locally manufactured product line of roller shades.
Main product pictures should be of roller shades, outdoor bug screens, awnings and outdoor pergolas.

Reason: I understand that Christmas is coming up real short and many people are extremely busy. If you have a CREATIVE gifting you still want to submit, I look forward to your idea!

Reason: Due to holiday season, we have not had sufficient time to review to make a final decision. Thank you for your patience!

Target Market(s)

High end home owners, designers, builders, architects

Industry/Entity Type

Contractor

Coding

Coded - Design and coding required

Number of Pages Required

3 page

Font styles to use
Sans Serif

Requirements
Must have
• Landing page with full size image like homepage of zolvane.it
• Products page that highlights products with simple product shot image, description and link to manufacturer.
• On main page a scrolling of customer reviews.
• I want a very simple, eye-catching, emotional image for homepage. It does not need to include any product image.
• An image that shows technology combining/meshing with hand craftsmanship.
• Focus is on design.
• http://www.zolvane.it/en/gallery is a great layout and design.
Nice to have
• Logo shape for icons and watermark should be used.
• Look like and have simple motion effects like quorix.com or mentaly7.com
Should not have
• Generic/standard looking feel like fellowpine.com or dimworksblinds.ca
• No use of green as background only subtle text.
• Lots of text and pages.

```html
<!DOCTYPE html>
<html lang="en">
<head>
<meta charset="utf-8">
<title>Velmar – Window Treatment Solutions</title>
<link rel="stylesheet" href="https://fonts.googleapis.com/css2?family=Montserrat:wght@400;500;600;700&family=Open+Sans:wght@400;600&display=swap">
<style>
:root{
  --green:#7cc142;
  --dark:#24272c;
  --darker:#17181b;
  --ink:#222;
  --muted:#666;
  --white:#fff;
  --sky:#a9c3d8;
  --pool:#2f93c4;
  --deck:#a68565;
  --wall:#eceae6;
}
*{box-sizing:border-box;margin:0;padding:0}
html,body{width:1200px;height:4186px;overflow:hidden;background:var(--white)}
body{position:relative;font-family:"Open Sans",Arial,sans-serif;color:var(--ink)}
.abs{position:absolute}
h2,h3,.brand,.nav a,.hero-title{font-family:"Montserrat",Arial,sans-serif}

/* hero */
.hero{left:0;top:0;width:1200px;height:710px;overflow:hidden}
.hero-photo{position:absolute;inset:0;background:
  linear-gradient(180deg,rgba(0,0,0,0) 0%,rgba(0,0,0,0) 100%),
  radial-gradient(ellipse 420px 260px at 190px 250px,#f4f3f0 0%,#e2e0dc 55%,rgba(226,224,220,0) 100%),
  radial-gradient(ellipse 360px 120px at 980px 320px,#5d7d4f 0%,rgba(93,125,79,0) 100%),
  linear-gradient(180deg,var(--sky) 0%,#d6e0e6 32%,#8fa08c 44%,var(--pool) 52%,#4fb2d8 60%,#c4a585 68%,var(--deck) 84%,#6f5641 100%)}
.hero-curve{position:absolute;left:0;bottom:0}
.logo{left:78px;top:46px}
.brand{font-size:44px;font-weight:600;color:var(--ink);line-height:1}
.brand-sub{font-size:15px;color:var(--ink);margin-top:4px}
.nav{left:486px;top:50px;width:714px;height:72px;background:rgba(255,255,255,.94);border-radius:36px 0 0 36px;display:flex;align-items:center;gap:34px;padding-left:36px}
.nav a{font-size:16px;color:#555;text-decoration:none;font-weight:500}
.nav a.active{color:var(--green)}
.hero-title{left:237px;top:315px;width:726px;height:98px;background:rgba(20,20,20,.72);color:var(--white);font-size:54px;font-weight:400;display:flex;align-items:center;justify-content:center}
.hero-sub{left:237px;top:424px;width:726px;height:36px;background:var(--green);color:var(--white);font-size:20px;display:flex;align-items:center;justify-content:center;letter-spacing:.3px}

/* products */
.product{top:792px;display:flex;gap:14px}
.product-photo{width:210px;height:156px}
.product h3{font-size:25px;font-weight:500;color:var(--green);margin-top:-2px}
.product h3 b{font-weight:600}
.product p{font-size:15px;line-height:1.55;color:var(--muted);width:300px;margin-top:6px}
.btn{display:inline-flex;align-items:center;gap:10px;margin-top:18px;height:52px;padding:0 30px;border:2px solid #333;border-radius:26px;font-family:"Montserrat",Arial,sans-serif;font-size:18px;font-weight:500;color:var(--ink)}

/* services */
.svc{left:0;width:1200px}
.svc.dark{color:var(--white)}
.section-title{left:0;width:1200px;text-align:center;font-size:40px;font-weight:500;font-family:"Montserrat",Arial,sans-serif}
.svc-title{font-size:34px;font-weight:500;text-transform:uppercase}
.dark .svc-title{color:var(--green)}
.light .svc-title{color:var(--ink)}
.svc-text{font-size:15px;line-height:1.65;width:560px;margin-top:14px}
.dark .svc-text{color:#ddd}
.light .svc-text{color:#444}
.icon{width:200px;height:200px}

/* testimonials */
.reviews{left:0;top:2505px;width:1200px;height:385px;background:radial-gradient(circle at 50% 40%,#2a2a2a,var(--darker))}
.reviews h2{font-size:40px;font-weight:500;color:var(--white)}
.reviews h2 span,.gallery h2 span{color:var(--green)}
.quote-mark{left:0;width:1200px;text-align:center;top:120px;font-family:Georgia,serif;font-size:90px;color:var(--green);line-height:1}
.quote{left:110px;width:980px;top:205px;text-align:center;font-size:16px;line-height:1.7;color:#eee}
.client{left:0;width:1200px;top:282px;text-align:center;font-size:15px;color:var(--green)}
.dots{left:0;width:1200px;top:315px;display:flex;justify-content:center;gap:8px}
.dots i{width:12px;height:12px;border-radius:50%;background:#ddd;display:block}
.dots i.on{background:var(--green)}

/* gallery */
.gallery h2{font-size:40px;font-weight:500;color:var(--ink)}
.gallery-intro{left:220px;width:760px;top:3010px;text-align:center;font-size:15px;line-height:1.7;color:var(--muted)}
.filters{left:200px;top:3088px;display:flex;gap:12px}
.filters span{height:52px;padding:0 34px;border:1px solid #ccc;border-radius:26px;display:flex;align-items:center;font-size:16px;color:#777}
.filters span.on{background:#111;color:var(--white);border-color:#111}
.grid{left:0;top:3166px;width:1200px;display:grid;grid-template-columns:repeat(4,300px);grid-template-rows:210px 210px}
.tile{position:relative}
.tile.hover::after{content:"";position:absolute;inset:0;background:rgba(124,193,66,.75)}

/* partners */
.partners{left:80px;top:3640px;width:1040px;display:flex;justify-content:space-between;align-items:center}
.partner{font-family:"Open Sans",Arial,sans-serif;font-size:24px;font-weight:600;color:#555}

/* footer */
.footer{left:0;top:3745px;width:1200px;height:441px}
.footer-bg{position:absolute;left:0;width:1200px;background:linear-gradient(180deg,#3a3a38,#262624)}
.footer h4{font-family:"Montserrat",Arial,sans-serif;font-size:19px;font-weight:500;color:var(--white);letter-spacing:1px}
.links{left:80px;top:140px}
.links li{list-style:none;font-size:15px;color:#bbb;margin-top:14px}
.links li:first-of-type{color:var(--white)}
.contact{left:346px;top:140px}
.contact-row{display:flex;gap:14px;margin-top:16px;font-size:15px;color:#ddd;line-height:1.5}
.contact-row svg{flex:none;margin-top:3px}
.contact-row .green{color:var(--green)}
.map{left:625px;top:145px;width:190px;height:190px;border-radius:50%;background:linear-gradient(135deg,#eeece6,#d8ddd3);border:5px solid #fff}
.map svg{position:absolute;left:78px;top:56px}
.f-logo{left:905px;top:170px}
.f-logo .brand{color:var(--white);font-size:30px}
.social{left:920px;top:245px;display:flex;gap:14px}
.social i{width:44px;height:44px;border-radius:50%;border:2px solid var(--white);display:block}
.copy{left:0;top:4130px;width:1200px;height:56px;background:#111;color:#ccc;font-size:15px;display:flex;align-items:center;justify-content:center}
.copy b{color:var(--white);margin:0 4px}
</style>
</head>
<body>

<header class="abs hero">
  <div class="hero-photo" role="img" aria-label="Modern white villa with open glass walls, a long blue swimming pool and a stone deck under a pale sky"></div>
  <svg class="hero-curve" width="1200" height="140" viewBox="0 0 1200 140"><path d="M0 40 Q600 170 1200 20 L1200 140 L0 140Z" fill="#fff"/></svg>
</header>
<div class="abs logo">
  <div class="brand">Velmar</div><div class="brand-sub">Window Treatment Solutions</div>
</div>
<nav class="abs nav">
  <a class="active">HOME</a><a>ABOUT</a><a>SERVICES</a><a>PRODUCTS</a><a>GALLERY</a><a>CONTACT</a>
</nav>
<div class="abs hero-title">Roman Skylight System</div>
<div class="abs hero-sub">INSTANT HEAT REDUCTION USING ROLLERS, OR STATIONARY SCREENS.</div>

<section class="abs product" style="left:78px">
  <div class="product-photo" role="img" aria-label="Bright window with sheer curtains and white flowers in a vase on the sill" style="background:radial-gradient(ellipse 60px 50px at 130px 110px,#b6a8cf,rgba(182,168,207,0)),linear-gradient(90deg,#e9e8ec 0%,#fbfbfa 35%,#dfe6e6 70%,#c7cfc4 100%)"></div>
  <div>
    <h3>INDOOR <b>PRODUCT</b></h3>
    <p>Lorem Ipsum is dummy text of the printing and typesetting industry. Lorem Ipsum has been the industry's standard dummy text ever sinc 1500.</p>
    <span class="btn">VIEW ALL <svg width="16" height="14" viewBox="0 0 16 14"><path d="M2 2l5 5-5 5M8 2l5 5-5 5" fill="none" stroke="#222" stroke-width="2"/></svg></span>
  </div>
</section>
<section class="abs product" style="left:620px">
  <div class="product-photo" role="img" aria-label="White two-storey house with a grey roof, green lawn and trees" style="background:radial-gradient(ellipse 80px 60px at 110px 80px,#f2f2f0,rgba(242,242,240,0)),linear-gradient(180deg,#9cc4e6 0%,#cfe0ec 35%,#8e9aa3 50%,#e8e8e4 62%,#5f8f3a 85%,#4c7a2d 100%)"></div>
  <div>
    <h3>OUTDOOR <b>PRODUCT</b></h3>
    <p>Lorem Ipsum is dummy text of the printing and typesetting industry. Lorem Ipsum has been the industry's standard dummy text ever sinc 1500.</p>
    <span class="btn">VIEW ALL <svg width="16" height="14" viewBox="0 0 16 14"><path d="M2 2l5 5-5 5M8 2l5 5-5 5" fill="none" stroke="#222" stroke-width="2"/></svg></span>
  </div>
</section>

<!-- services -->
<section class="abs svc dark" style="top:1010px;height:490px;background:linear-gradient(180deg,#2a2d31 0%,#3b3e43 45%,#4a4c4f 75%,#2b2d30 100%)" role="img" aria-label="Living room with dark roller shades lowered over tall windows">
  <svg class="abs" style="left:0;top:0" width="1200" height="60" viewBox="0 0 1200 60"><path d="M0 0 L1200 0 L1200 10 Q600 70 0 10Z" fill="#fff"/></svg>
  <h2 class="abs section-title" style="top:120px;color:var(--green)">SERVICES</h2>
  <div class="abs" style="left:78px;top:262px">
    <h3 class="svc-title">Roller Shades</h3>
    <p class="svc-text">Lorem Ipsum is simply dummy text of the printing and typesetting industry. Lorem Ipsum has been the industry's standard dummy text ever since the 1500s.</p>
  </div>
  <svg class="abs icon" style="left:787px;top:201px" viewBox="0 0 200 200"><circle cx="100" cy="100" r="92" fill="#fff"/><circle cx="100" cy="100" r="70" fill="none" stroke="#111" stroke-width="7"/><rect x="68" y="68" width="64" height="56" fill="none" stroke="#111" stroke-width="6"/><path d="M68 82h64M68 96h64M68 110h64" stroke="#111" stroke-width="4"/><rect x="64" y="124" width="72" height="8" fill="#111"/></svg>
</section>

<section class="abs svc light" style="top:1500px;height:333px;background:linear-gradient(90deg,#e4e3de 0%,#f6f6f3 30%,#fbfbf9 55%,#e9e8e3 100%)" role="img" aria-label="Bright room with sheer white drapery at the windows">
  <svg class="abs icon" style="left:207px;top:68px" viewBox="0 0 200 200"><circle cx="100" cy="100" r="92" fill="#fff"/><circle cx="100" cy="100" r="70" fill="none" stroke="#111" stroke-width="7"/><rect x="62" y="62" width="76" height="8" fill="#111"/><path d="M68 70v68h10Q78 100 96 76V70Z M132 70v68h-10Q122 100 104 76V70Z" fill="#111"/></svg>
  <div class="abs" style="left:555px;top:104px">
    <h3 class="svc-title">Drapery</h3>
    <p class="svc-text">Lorem Ipsum is simply dummy text of the printing and typesetting industry. Lorem Ipsum has been the industry's standard dummy text ever since the 1500s.</p>
  </div>
</section>

<section class="abs svc dark" style="top:1833px;height:332px;background:linear-gradient(180deg,#25272b 0%,#3c3e44 40%,#4a3232 60%,#2a2b2f 100%)" role="img" aria-label="Dark red retractable awning over an evening terrace">
  <div class="abs" style="left:78px;top:100px">
    <h3 class="svc-title">Awnings</h3>
    <p class="svc-text">Lorem Ipsum is simply dummy text of the printing and typesetting industry. Lorem Ipsum has been the industry's standard dummy text ever since the 1500s.</p>
  </div>
  <svg class="abs icon" style="left:787px;top:70px" viewBox="0 0 200 200"><circle cx="100" cy="100" r="92" fill="#fff"/><circle cx="100" cy="100" r="70" fill="none" stroke="#111" stroke-width="7"/><path d="M62 70h76l6 22H56Z" fill="#111"/><rect x="66" y="92" width="68" height="44" fill="none" stroke="#111" stroke-width="6"/><rect x="88" y="108" width="24" height="28" fill="#111"/></svg>
</section>

<section class="abs svc light" style="top:2165px;height:345px;background:linear-gradient(90deg,#e8e2d6 0%,#f5f3ef 25%,#ece6da 50%,#f6f4f0 75%,#e6dfd1 100%)" role="img" aria-label="Sunroom with woven shades and screened openings">
  <svg class="abs icon" style="left:207px;top:73px" viewBox="0 0 200 200"><circle cx="100" cy="100" r="92" fill="#fff"/><circle cx="100" cy="100" r="70" fill="none" stroke="#111" stroke-width="7"/><rect x="66" y="64" width="68" height="60" fill="none" stroke="#111" stroke-width="6"/><path d="M76 74h48v40H76Z" fill="none" stroke="#111" stroke-width="2"/><rect x="60" y="124" width="80" height="8" fill="#111"/></svg>
  <div class="abs" style="left:555px;top:100px">
    <h3 class="svc-title">Bug Screens</h3>
    <p class="svc-text">Lorem Ipsum is simply dummy text of the printing and typesetting industry. Lorem Ipsum has been the industry's standard dummy text ever since the 1500s.</p>
  </div>
</section>

<!-- testimonials -->
<section class="abs reviews">
  <svg class="abs" style="left:0;top:0" width="1200" height="50" viewBox="0 0 1200 50"><path d="M0 0 L1200 0 Q600 70 0 0Z" fill="#ece7dc"/></svg>
  <h2 class="abs section-title" style="top:62px">WHAT OUR <span>CLIENT SAY</span></h2>
  <div class="abs quote-mark">&ldquo;</div>
  <p class="abs quote">&ldquo;Lorem Ipsum is simply dummy text of the printing and typesetting industry. Lorem Ipsum has been the industry's standard dummy text ever since the 1500s, when an unknown printer took a galley of type and scrambled it to make a&rdquo;</p>
  <div class="abs client">&mdash; CLIENT NAME</div>
  <div class="abs dots"><i></i><i class="on"></i><i></i><i></i></div>
</section>

<!-- gallery -->
<section class="gallery">
  <h2 class="abs section-title" style="top:2940px">OUR <span>GALLARY</span></h2>
  <p class="abs gallery-intro">Lorem Ipsum is simply dummy text of the printing and typesetting industry. Lorem Ipsum has been the industry's standard dummy text ever since the 1500s, when an unknown printer took a</p>
  <div class="abs filters"><span class="on">All</span><span>Roller Shades</span><span>Drapery</span><span>Outdoor Bug Screens</span><span>Awnings</span></div>
  <div class="abs grid">
    <div class="tile" role="img" aria-label="Covered patio with dining set behind outdoor screens" style="background:linear-gradient(180deg,#3a3f3d 0%,#cfd6d4 30%,#9fa9a2 60%,#4d544f 100%)"></div>
    <div class="tile" role="img" aria-label="Living room with lowered sheer screens" style="background:linear-gradient(180deg,#5d6260 0%,#d9dcd8 35%,#b9bab4 65%,#6b6a64 100%)"></div>
    <div class="tile hover" role="img" aria-label="Glass wall opening to a green valley" style="background:linear-gradient(180deg,#b9cfd8,#7ea05a)">
      <svg style="position:absolute;left:125px;top:80px;z-index:1" width="50" height="50" viewBox="0 0 50 50"><circle cx="21" cy="21" r="15" fill="none" stroke="#fff" stroke-width="4"/><path d="M32 32l13 13M21 14v14M14 21h14" stroke="#fff" stroke-width="4"/></svg>
    </div>
    <div class="tile" role="img" aria-label="Terrace lounge with a stone fireplace" style="background:linear-gradient(135deg,#c9b9a4 0%,#8c6f55 40%,#3d2f26 100%)"></div>
    <div class="tile" role="img" aria-label="Pergola with white vertical screens" style="background:linear-gradient(160deg,#f2f3f4 0%,#d6d9dc 45%,#7b8184 100%)"></div>
    <div class="tile" role="img" aria-label="Outdoor lounge under a pergola roof" style="background:linear-gradient(180deg,#2f3433 0%,#a9b1b0 40%,#6f7774 70%,#353a38 100%)"></div>
    <div class="tile" role="img" aria-label="Screened view over wooded hills" style="background:linear-gradient(180deg,#d6e2e8 0%,#a9bfcb 40%,#6e8457 70%,#4d5e3d 100%)"></div>
    <div class="tile" role="img" aria-label="Deck with chairs behind clear screens" style="background:linear-gradient(180deg,#d2dee6 0%,#9fb2bd 40%,#55605a 75%,#2c312f 100%)"></div>
  </div>
</section>

<!-- partners -->
<div class="abs partners">
  <span class="partner">Brindex</span><span class="partner">Harvex</span><span class="partner">Quietrail</span><span class="partner">Lumio</span><span class="partner">Ferrand</span><span class="partner">Solvaro</span>
</div>

<!-- footer -->
<footer class="abs footer">
  <svg class="abs" style="left:0;top:0" width="1200" height="90" viewBox="0 0 1200 90"><path d="M0 90 L0 60 Q500 -40 1200 40 L1200 90Z" fill="var(--green)"/><path d="M0 90 L0 80 Q500 -10 1200 60 L1200 90Z" fill="#3a3a38"/></svg>
  <div class="footer-bg" style="top:80px;height:306px"></div>
  <div class="abs links"><h4>USEFUL LINKS</h4><ul><li>Home</li><li>Blog</li><li>Privacy Policy</li><li>Terms of Use</li><li>Contact Us</li></ul></div>
  <div class="abs contact"><h4>CONTACT US</h4>
    <div class="contact-row"><svg width="16" height="22" viewBox="0 0 16 22"><path d="M8 0a8 8 0 0 1 8 8c0 6-8 14-8 14S0 14 0 8a8 8 0 0 1 8-8z" fill="#fff"/><circle cx="8" cy="8" r="3" fill="#333"/></svg><div><span class="green">VELMAR</span><br>27B-14 Harwick Ave,<br>Toronto, ON, M4B 2K8</div></div>
    <div class="contact-row"><svg width="16" height="16" viewBox="0 0 16 16"><path d="M3 1l3 3-2 2q2 4 6 6l2-2 3 3-2 2Q6 15 1 3Z" fill="#fff"/></svg><div>416-555-0142</div></div>
    <div class="contact-row"><svg width="16" height="12" viewBox="0 0 16 12"><rect width="16" height="12" fill="#fff"/><path d="M0 0l8 7 8-7" fill="none" stroke="#333" stroke-width="1.5"/></svg><div>info@velmarblinds.ca</div></div>
  </div>
  <div class="abs map" role="img" aria-label="Street map showing the showroom location"><svg width="24" height="34" viewBox="0 0 16 22"><path d="M8 0a8 8 0 0 1 8 8c0 6-8 14-8 14S0 14 0 8a8 8 0 0 1 8-8z" fill="#e0473c"/><circle cx="8" cy="8" r="3" fill="#fff"/></svg></div>
  <div class="abs f-logo"><div class="brand">Velmar</div><div class="brand-sub" style="color:#ddd;font-size:12px">Window Treatment Solutions</div></div>
  <div class="abs social"><i></i><i></i><i></i></div>
</footer>
<div class="abs copy">&copy; <b>VELMAR</b> - 2016. All Rights Reserved</div>

</body>
</html>
```